integrative health clinic-Medical massage, acupuncture, chiropractic

we like our logo, but are open to new ideas. We need a new card design. We have added chiropractic and acupuncture that we have put under the name of the business. We are an integrative medical clinic

Target Market(s)

General public, athletes

Contact Information for Business Card

Phone 5055583927
Fax 5055583926
Hours Monday-Friday 9-6
Saturday 10-6
The 20% can be smaller on the back

Colors
3176b5
0355a3

Requirements
Must have
• Logo but am open to ideas
Nice to have
• We are an integrated medical clinic but also want to be personable. We want the card fun and inviting

```html
<!DOCTYPE html>
<html lang="en">
<head>
<meta charset="utf-8">
<title>Kindred Motion Wellness — Business Card</title>
<link href="https://fonts.googleapis.com/css2?family=Open+Sans:ital,wght@0,300;0,400;0,700;1,700&family=Montserrat:wght@700&display=swap" rel="stylesheet">
<style>
  :root {
    --brand-blue: #0a40fc;
    --ink: #111111;
    --paper: #ffffff;
    --stage: #e6e7e9;
    --mark-grey: #9a9a9a;
  }
  * { box-sizing: border-box; margin: 0; padding: 0; }
  html, body { width: 848px; height: 1200px; overflow: hidden; }
  body {
    background: var(--stage);
    font-family: "Open Sans", Arial, sans-serif;
    position: relative;
  }
  .card { position: absolute; overflow: hidden; }

  /* Front */
  .card-front { left: 123px; top: 214px; width: 630px; height: 382px; background: var(--paper); }
  .brand-lockup {
    position: absolute; left: 0; right: 0; top: 250px; top: 36px;
    display: flex; justify-content: center; align-items: center; gap: 12px;
  }
  .brand-dot { width: 22px; height: 22px; border-radius: 50%; background: var(--brand-blue); }
  .brand-name { font-weight: 700; font-size: 34px; color: var(--ink); letter-spacing: -0.5px; }
  .services {
    position: absolute; left: 0; right: 0; top: 152px; text-align: center;
    font-weight: 700; font-style: italic; font-size: 16px; letter-spacing: 0.4px;
    color: var(--brand-blue);
  }
  .info-band {
    position: absolute; left: 0; top: 180px; width: 100%; height: 158px;
    background: var(--brand-blue); color: var(--paper);
  }
  .person-name { position: absolute; left: 22px; top: 28px; font-weight: 700; font-size: 21px; }
  .person-title { position: absolute; left: 22px; top: 56px; font-weight: 300; font-size: 22px; }
  .person-email { position: absolute; left: 22px; top: 124px; font-weight: 300; font-size: 15px; }
  .hours { position: absolute; left: 386px; width: 158px; top: 32px; text-align: center; font-size: 12px; line-height: 22px; }
  .contact-list { position: absolute; left: 425px; top: 86px; list-style: none; font-size: 11px; }
  .contact-list li { display: flex; align-items: center; gap: 10px; height: 20px; }
  .contact-list svg { width: 14px; height: 14px; }
  .offer-strip {
    position: absolute; left: 0; top: 351px; width: 100%; height: 17px;
    background: var(--brand-blue); color: var(--paper);
    font-family: "Montserrat", Arial, sans-serif; font-weight: 700; font-size: 12px;
    letter-spacing: 1.2px; text-align: center; line-height: 17px;
  }

  /* Back */
  .card-back { left: 115px; top: 675px; width: 645px; height: 390px; background: var(--brand-blue); }
  .back-lockup {
    position: absolute; left: 0; right: 0; top: 160px;
    display: flex; justify-content: center; align-items: center; gap: 16px;
  }
  .back-dot { width: 34px; height: 34px; border-radius: 50%; background: var(--mark-grey); }
  .back-name { font-weight: 700; font-size: 44px; color: var(--mark-grey); letter-spacing: -1px; }
</style>
</head>
<body>
  <section class="card card-front">
    <div class="brand-lockup">
      <span class="brand-dot"></span>
      <span class="brand-name">Kindred Motion Wellness</span>
    </div>
    <p class="services">CHIROPRACTIC AND ACUPUNCTURE</p>
    <div class="info-band">
      <p class="person-name">FULL NAME</p>
      <p class="person-title">Company Designation</p>
      <p class="person-email">Email-id</p>
      <p class="hours">Monday-Friday 9-6<br>Saturday 10-6</p>
      <ul class="contact-list">
        <li>
          <svg viewBox="0 0 14 14" aria-label="Phone"><rect x="1" y="1" width="12" height="12" rx="2" fill="#fff"/><path d="M5 3.5c-1 .6-1.3 2.8 0 5s3 3 4 2.5l-.8-1.6-1.2.4c-.7-.6-1.2-1.6-1.4-2.5l1-.7z" fill="var(--brand-blue)"/></svg>
          <span>5055583927</span>
        </li>
        <li>
          <svg viewBox="0 0 14 14" aria-label="Fax" fill="none" stroke="#fff" stroke-width="1"><rect x="1" y="2" width="9" height="8"/><rect x="3" y="2" width="5" height="3"/><path d="M11 7v6M9 11l2 2 2-2"/></svg>
          <span>5055583926</span>
        </li>
      </ul>
    </div>
    <p class="offer-strip">20% OFF FIRST VISIT</p>
  </section>

  <section class="card card-back">
    <div class="back-lockup">
      <span class="back-dot"></span>
      <span class="back-name">Kindred Motion Wellness</span>
    </div>
  </section>
</body>
</html>
```